Venneputt.dk - FriendPutt

I need a design for a WordPress site that serves to inform and present the national golfchampionship for colleagues in Denmark. The sites need to be visual stuninng or big, and it doesnt have a lot of pages. Maybe 5-6 regular text pages and not a lot of navigation. It should be a simple and powerfull site.

The sites need to present and sell the tournament, and have a clear call to action button "Sign up" (Tilmeld) and resultscoring.

If you can make a logo and visual ID for the tournament as well that would be a bonus.

Target Market(s)

Golfers

Logo Text

Venneputt

Number of Pages Required

3 page

Requirements
Must have
• A frontpage
• Button 1 - Tilmeld (danish for sign up)
• Button 2 - Resultater (results)
Nice to have
• Logo
• A style we can use offline as well

```html
<!DOCTYPE html>
<html lang="da">
<head>
<meta charset="utf-8">
<title>Venneputt.dk – Danmarks sjoveste kollegaturnering i golf</title>
<link rel="stylesheet" href="https://fonts.googleapis.com/css2?family=Ubuntu:wght@300;400;500;700&display=swap">
<style>
:root{
  --red:#e3231f;
  --purple:#a02ff0;
  --link:#5a4fc4;
  --ink:#222;
  --muted:#555;
  --band:#efefef;
  --line:#dcdcdc;
  --white:#fff;
}
*{box-sizing:border-box;margin:0;padding:0}
html,body{width:1200px;height:2699px;overflow:hidden;background:var(--white)}
body{font-family:"Ubuntu",Arial,sans-serif;color:var(--ink);position:relative}

/* Hero */
.hero{position:absolute;left:0;top:0;width:1200px;height:590px}
.hero-photo{position:absolute;inset:0;
  background:
   linear-gradient(180deg,rgba(255,255,255,.85) 0%,rgba(255,255,255,0) 22%),
   radial-gradient(ellipse at 25% 55%,#3a4a1c 0%,#5a7a22 30%,transparent 55%),
   linear-gradient(90deg,#4d6b1c 0%,#7ea038 35%,#9fc45a 60%,#8fba4c 100%)}
.site-header{position:absolute;left:173px;right:173px;top:20px;height:60px;display:flex;align-items:center;justify-content:space-between}
.brand{display:flex;align-items:center;gap:20px}
.brand-name{font-weight:700;font-size:18px;color:var(--red)}
.brand-divider{width:1px;height:44px;background:#bbb}
.brand-partner{font-weight:700;font-size:13px;line-height:14px;color:#333;text-transform:uppercase;display:flex;align-items:center;gap:8px}
.brand-partner .dot{width:26px;height:26px;border-radius:50%;background:#3b8ed8}
.main-nav{display:flex;gap:40px;font-size:11px;font-weight:500;color:#333;text-transform:uppercase}
.hero-title{position:absolute;left:0;right:0;top:218px;text-align:center;color:var(--white)}
.hero-title h1{font-size:34px;font-weight:700;text-shadow:0 2px 6px rgba(0,0,0,.35)}
.hero-title p{font-size:32px;font-weight:300;margin-top:8px;text-shadow:0 2px 6px rgba(0,0,0,.35)}
.hero-actions{position:absolute;top:364px;left:0;right:0;display:flex;justify-content:center;gap:56px}
.btn{width:186px;height:58px;border-radius:29px;display:flex;align-items:center;justify-content:center;font-size:24px;box-shadow:0 4px 10px rgba(0,0,0,.25)}
.btn-signup{background:var(--red);color:var(--white);font-weight:700;width:158px}
.btn-results{background:var(--white);color:var(--ink);font-weight:500}

/* Key facts band */
.facts{position:absolute;top:590px;left:0;width:1200px;height:270px;background:var(--band);text-align:center;font-size:21px;font-weight:300;color:#333}
.facts p{position:absolute;left:0;right:0}

/* Tournament text */
.details{position:absolute;top:912px;left:170px;right:170px;text-align:center;font-size:11.5px;line-height:18px;color:#444;font-weight:300}
.details h3{font-size:12px;font-weight:500;color:var(--ink);margin:20px 0 17px}
.details h3:first-child{margin-top:0}
.details .gap{height:18px}
.details h2{font-size:23px;font-weight:400;color:var(--ink);text-decoration:underline;text-underline-offset:4px;margin:20px 0 14px}

/* Downloads */
.more-title{position:absolute;top:1958px;left:0;right:0;text-align:center;font-size:29px;font-weight:500}
.doc{position:absolute;display:flex;gap:18px;align-items:flex-start}
.doc svg{flex:none}
.doc-name{font-size:17px;color:var(--link);line-height:22px}
.doc-size{font-size:16px;color:var(--link);font-weight:300}
.participants{position:absolute;top:2278px;left:0;right:0;text-align:center;font-size:19px;color:var(--red);display:flex;justify-content:center;align-items:center;gap:12px}

/* Footer area */
.btn-contact{position:absolute;left:173px;top:2362px;width:196px;height:44px;border-radius:22px;background:var(--purple);color:var(--white);font-weight:500;font-size:18px;display:flex;align-items:center;justify-content:center;box-shadow:0 4px 8px rgba(0,0,0,.25)}
.contact-photo{position:absolute;left:194px;top:2448px;width:157px;height:76px;background:linear-gradient(180deg,#8b6b52,#5a4032)}
.contact-card{position:absolute;left:150px;top:2552px;width:245px;text-align:center;font-size:17px;line-height:23px;color:#333}
.contact-card strong{font-weight:700;font-size:19px;color:var(--ink)}
.contact-card a{color:var(--link);text-decoration:none}
.partner-note{position:absolute;left:455px;top:2375px;font-size:9px;color:#333}
.partner-name{position:absolute;left:455px;top:2390px;font-size:17px;font-weight:500;color:#333}
.sponsor{position:absolute;left:458px;top:2550px;font-size:24px;font-weight:500;color:#333}
.video-caption{position:absolute;left:725px;top:2398px;font-size:17px;color:#888;font-weight:300}
.video{position:absolute;left:725px;top:2435px;width:303px;height:202px;background:linear-gradient(180deg,#a9c4e6 0%,#8fb0d2 35%,#5f7f3b 60%,#4d6a2c 100%)}
.video-bar{position:absolute;left:0;right:0;bottom:0;height:14px;background:#e8e8e8}
.video-play{position:absolute;left:128px;top:82px}

.site-footer{position:absolute;left:0;right:0;top:2668px;height:31px;border-top:1px solid var(--line);display:flex;justify-content:center;gap:34px;font-size:9px;color:#777;align-items:center}
</style>
</head>
<body>

<section class="hero">
  <div class="hero-photo" role="img" aria-label="Golfbag med køller på en grøn golfbane"></div>
  <header class="site-header">
    <div class="brand">
      <span class="brand-name">NGF</span>
      <span class="brand-divider"></span>
      <span class="brand-partner"><span class="dot"></span>Nordisk<br>Firmasport</span>
    </div>
    <nav class="main-nav">
      <span>Home</span><span>Entry forms</span><span>About us</span><span>2014 Tournament</span><span>Gallery</span><span>Contact us</span>
    </nav>
  </header>
  <div class="hero-title">
    <h1>Danmarks sjoveste kollegaturnering i golf.</h1>
    <p>Spil mod andre spillere på nye baner.</p>
  </div>
  <div class="hero-actions">
    <span class="btn btn-signup">Tilmeld</span>
    <span class="btn btn-results">Resultater</span>
  </div>
</section>

<section class="facts">
  <p style="top:70px">Tidspunkt: 1. maj 2015 kl. 07:00 - 18. sep 2015 kl. 21:30</p>
  <p style="top:120px">Kontakt: Mette Kjærgaard , Tlf. 64123456</p>
  <p style="top:168px">Tilmeldingsfrist: 27. april 2015</p>
</section>

<section class="details">
  <h3>Turneringen afvikles i 2015 for 8. gang.</h3>
  <p>Finalestævnet er i år på Kildemose Golfklubs bane på Fyn.<br>Vær med, og vind rejsegavekort for hele holdet på op til kr. 22.000,- som 1. præmie, dog max. kr. 5.500,- pr. deltager, jf. amatørbestemmelserne.</p>
  <h3>Pris</h3>
  <p>Kr. 500,- pr. hold.</p>
  <h3>Deltagere</h3>
  <p>Turneringen er åben for alle klubgolfere med gyldigt NGF-kort, gyldigt EGA handicap og amatørstatus.</p>
  <div class="gap"></div>
  <h3>Hold og puljer</h3>
  <p>Et hold består af 2-4 spillere med to spillere fra holdet pr. match. Turneringen kører i puljer á 5-6 hold, som er delt op geografisk, efter hvor i landet I kommer fra. Puljens holdkaptajner aftaler selv indbyrdes tid og sted for den enkelte match - så I kan spille, hvor og hvornår det passer jer.<br>Alle betaler egen greenfee.</p>
  <h3>Spilleform</h3>
  <p>Spilleformen er en fourball - high/low hulspilsturnering, hvor 2 spillere fra holdet spiller med 2 spillere fra et andet hold.<br>Læs mere i turneringsbetingelserne, som du finder her på siden.</p>
  <h3>Stopdatoer</h3>
  <p>Runde 1: 18. maj<br>Runde 2: 8. juni<br>Runde 3: 29. juni<br>Runde 4: 17. august<br>Runde 5: 7. september</p>
  <h3>Finalestævne fredag den 18. september 2015</h3>
  <p>Vinderne fra hver pulje kvalificerer sig til at deltage i finalestævnet, som spilles på Kildemose Golfklub, Lærkestien 14, 5491 Kildemose fredag den 18. september 2015 kl. 10.00.<br>Finalen bliver spillet som stableford four-ball best-ball med 7/8 handicap og med gunstart.<br>Finalestævnet spilles af to spillere fra hvert hold. Greenfee og middag betales af Nordisk Firmasport.</p>
  <h3>Præmier</h3>
  <p>Puljevindernes præmie er deltagelse i finalestævnet.<br>Nordisk Firmasport betaler greenfee, sportsbolle, vand og middag til finalestævnet.</p>
  <h2>Finalepræmier</h2>
  <p>1. præmie: Et rejsegavekort på op til kr. 22.000,- pr. hold, dog max. kr. 5.500,- pr. tilmeldt spiller.<br>2. præmie: Et gavekort til golfudstyr på kr. 2000,- pr. hold.<br>3. præmie: Et gavekort til golfudstyr på kr. 1000,- pr. hold.</p>
  <div class="gap"></div><div class="gap"></div>
  <p>På finaledagen er der derudover præmie til længste drive og nærmest flaget.</p>
</section>

<h2 class="more-title">Mere information</h2>

<svg width="0" height="0" style="position:absolute">
  <defs>
    <symbol id="pdf-icon" viewBox="0 0 46 52">
      <path d="M6 2h26l10 10v38H6z" fill="#f4f4f4" stroke="#bbb"/>
      <path d="M32 2v10h10" fill="#ddd" stroke="#bbb"/>
      <rect x="0" y="6" width="26" height="13" fill="#e3231f"/>
      <text x="13" y="16" font-size="9" font-weight="700" fill="#fff" text-anchor="middle" font-family="Ubuntu,Arial,sans-serif">PDF</text>
      <path d="M14 44c6-10 10-22 8-26s-6 4 2 14 14 8 10 6-16 0-20 6z" fill="none" stroke="#e3231f" stroke-width="2"/>
    </symbol>
  </defs>
</svg>

<div class="doc" style="left:261px;top:2058px"><svg width="46" height="52"><use href="#pdf-icon"/></svg><div><div class="doc-name">Puljer</div><div class="doc-size">(PDF, 203 KB)</div></div></div>
<div class="doc" style="left:482px;top:2058px"><svg width="46" height="52"><use href="#pdf-icon"/></svg><div><div class="doc-name">Turneringsplan</div><div class="doc-size">(PDF, 339 KB)</div></div></div>
<div class="doc" style="left:720px;top:2058px"><svg width="46" height="52"><use href="#pdf-icon"/></svg><div><div class="doc-name">Turneringsbetingelser</div><div class="doc-size">(PDF, 84 KB)</div></div></div>
<div class="doc" style="left:238px;top:2162px"><svg width="46" height="52"><use href="#pdf-icon"/></svg><div><div class="doc-name">Holdkaptajner</div><div class="doc-size">(PDF, 254 KB)</div></div></div>
<div class="doc" style="left:464px;top:2162px"><svg width="46" height="52"><use href="#pdf-icon"/></svg><div><div class="doc-name">7_8_handicaptabel</div><div class="doc-size">(PDF, 102 KB)</div></div></div>
<div class="doc" style="left:733px;top:2162px"><svg width="46" height="52"><use href="#pdf-icon"/></svg><div><div class="doc-name">Ofte stillede spørgsmål</div><div class="doc-size">(PDF, 89 KB)</div></div></div>

<div class="participants">Deltagerliste (opdateres løbende)
  <svg width="26" height="26" viewBox="0 0 26 26"><circle cx="13" cy="13" r="11.5" fill="none" stroke="#e3231f" stroke-width="2"/><path d="M8 13h10M14 9l4 4-4 4" fill="none" stroke="#e3231f" stroke-width="2"/></svg>
</div>

<span class="btn-contact">Kontakt</span>
<div class="contact-photo" role="img" aria-label="Portræt af generalsekretæren"></div>
<div class="contact-card">
  <strong>Per Vestergaard</strong><br>Generalsekretær<br>Tlf: 40 11 22 33<br>Mail: <a>pv@firmasport.dk</a>
</div>

<div class="partner-note">I samarbejde med:</div>
<div class="partner-name">Dansk Golfring</div>
<div class="sponsor">Holm Rejser</div>

<div class="video-caption">Se video fra Venneputt finalen 2011</div>
<div class="video" role="img" aria-label="Videostill fra finalen med to golfspillere på banen">
  <svg class="video-play" width="46" height="38" viewBox="0 0 46 38"><rect width="46" height="38" rx="4" fill="rgba(0,0,0,.6)"/><path d="M18 11l12 8-12 8z" fill="#fff"/></svg>
  <div class="video-bar"></div>
</div>

<footer class="site-footer">
  <span>Nordisk Firmasport</span><span>Havnegade 8, 5800 Strandby</span><span>Tlf. 64 20 30 40</span><span>kontakt@firmasport.dk</span>
</footer>

</body>
</html>
```